Business Card for a Wedding Films Business

We require a business card design for our business 'Lewis Marrow Wedding Films'. The logo needs to look classy and high end.

Target Market(s)

Wedding Couples

Contact Information for Business Card

Lewis Marrow Wedding Films
07312 605 227
films@lewismarrowreels.com
www.lewismarrowreels.com

Facebook: @lewismarrowweddingfilms
Instagram: @lewismarrowfilms

Font styles to use
Sans Serif

Requirements
Must have
• Social media icons - Facebook and Instagram

```html
<!DOCTYPE html>
<html lang="en">
<head>
<meta charset="utf-8">
<title>Lewis Marrow Wedding Films – Business Card</title>
<link rel="stylesheet" href="https://fonts.googleapis.com/css2?family=Josefin+Sans:wght@600;700&family=Lato:wght@400&display=swap">
<style>
  :root{
    --backdrop:#2a2a2a;
    --card-white:#f2f2f2;
    --ink:#111111;
    --gold:#a38a4e;
    --film-dark:#0c0c0c;
    --film-mid:#3a3a3a;
    --sprocket:#f7f7f7;
    --light:#ffffff;
  }
  *{box-sizing:border-box;margin:0;padding:0}
  html,body{width:1200px;height:900px;overflow:hidden}
  body{background:var(--backdrop);position:relative;font-family:"Lato",sans-serif}

  .card{position:absolute;width:560px;height:320px;border-radius:16px;overflow:hidden}

  /* Front */
  .card-front{left:80px;top:70px;background:var(--card-white);
    border-top:5px solid var(--ink);border-right:5px solid var(--ink);
    border-left:5px solid var(--gold);border-bottom:5px solid var(--gold)}
  .brand-name{font-family:"Josefin Sans",sans-serif;text-transform:uppercase;text-align:center;line-height:1.2}
  .brand-title{display:block;font-weight:700;font-size:24px;letter-spacing:.3em}
  .brand-sub{display:block;font-weight:600;font-size:11px;letter-spacing:.6em;margin-top:4px}
  .card-front .brand-name{position:absolute;left:0;right:0;top:50%;transform:translateY(-50%);color:var(--ink)}

  /* Back */
  .card-back{left:560px;top:510px;background:var(--card-white)}
  .film-band{position:absolute;inset:0;
    background:linear-gradient(100deg,var(--film-dark) 0%,var(--film-mid) 50%,var(--film-dark) 100%);
    clip-path:polygon(0 48%,100% 20%,100% 100%,0 100%)}
  .sprocket{position:absolute;width:26px;height:18px;border-radius:4px;background:var(--sprocket);
    box-shadow:0 0 6px rgba(255,255,255,.6)}
  .card-back .brand-name{position:absolute;left:0;right:0;top:152px;color:var(--light)}
  .card-back .brand-title{font-size:22px}
  .contact-list,.social-list{position:absolute;list-style:none;color:var(--light);font-size:13px}
  .contact-list{left:56px;bottom:24px}
  .social-list{right:46px;bottom:44px}
  .contact-list li,.social-list li{display:flex;align-items:center;gap:8px;margin-top:6px}
  .contact-list svg{width:15px;height:15px;flex:none}
  .social-mark{width:14px;height:14px;border-radius:3px;border:1.5px solid var(--light);flex:none}
</style>
</head>
<body>

<section class="card card-front" aria-label="Business card front">
  <p class="brand-name"><span class="brand-title">Lewis Marrow</span><span class="brand-sub">Wedding Films</span></p>
</section>

<section class="card card-back" aria-label="Business card back">
  <div class="film-band"></div>

  <span class="sprocket" style="right:14px;top:82px"></span>
  <span class="sprocket" style="right:14px;top:120px"></span>
  <span class="sprocket" style="right:14px;top:158px"></span>
  <span class="sprocket" style="right:14px;top:196px"></span>

  <span class="sprocket" style="left:14px;top:172px"></span>
  <span class="sprocket" style="left:14px;top:210px"></span>
  <span class="sprocket" style="left:14px;top:248px"></span>
  <span class="sprocket" style="left:14px;top:286px"></span>

  <p class="brand-name"><span class="brand-title">Lewis Marrow</span><span class="brand-sub">Wedding Films</span></p>

  <ul class="contact-list">
    <li>
      <svg viewBox="0 0 16 16" fill="none" stroke="#fff" stroke-width="1.3"><path d="M3 2l3 1 1 3-2 1a8 8 0 004 4l1-2 3 1 1 3-2 1C7 14 2 9 2 4z"/></svg>
      07312 605 227
    </li>
    <li>
      <svg viewBox="0 0 16 16" fill="none" stroke="#fff" stroke-width="1.3"><rect x="1.5" y="3.5" width="13" height="9"/><path d="M1.5 3.5l6.5 5 6.5-5"/></svg>
      films@lewismarrowreels.com
    </li>
    <li>
      <svg viewBox="0 0 16 16" fill="none" stroke="#fff" stroke-width="1.2"><circle cx="8" cy="8" r="6.5"/><ellipse cx="8" cy="8" rx="3" ry="6.5"/><path d="M1.5 8h13M2.5 5h11M2.5 11h11"/></svg>
      www.lewismarrowreels.com
    </li>
  </ul>

  <ul class="social-list">
    <li><span class="social-mark"></span>@lewismarrowfilms</li>
    <li><span class="social-mark"></span>@lewismarrowweddingfilms</li>
  </ul>
</section>

</body>
</html>
```